Business Card Design Project

Want a modern business card.
Concern is that our email address is long and thus poses a design challenge.
Items like the company name can be omitted from text as it will be available via the logo.

Example:
Gerald Tunstall
President / CEO
Cell 555.304.1182
Office 555.617.2093
geraldt@korvantsolutionsgroup.example
www.korvantsolutionsgroup.example

Target Market(s)

Technical and executive level members of Information Technology companies in the Healthcare industry.

Industry/Entity Type

Business

Colors

Designer to choose colors to be used in the design.

Requirements
Nice to have
• Raised logo, but I am open.

```html
<!DOCTYPE html>
<html lang="en">
<head>
<meta charset="utf-8">
<title>Korvant Solutions Group – Business Card</title>
<link rel="stylesheet" href="https://fonts.googleapis.com/css2?family=Open+Sans:wght@600;700&display=swap">
<style>
  :root {
    --navy: #13296b;
    --red: #d9141b;
    --paper: #ffffff;
    --backdrop: #e9e7e3;
    --card-shadow: 0 10px 30px rgba(0, 0, 0, 0.18);
  }
  * { box-sizing: border-box; margin: 0; padding: 0; }
  html, body {
    width: 1200px;
    height: 900px;
    overflow: hidden;
    background: var(--backdrop);
    font-family: "Open Sans", Arial, sans-serif;
  }
  .stage {
    width: 1200px;
    height: 900px;
    display: flex;
    flex-direction: column;
    align-items: center;
    justify-content: center;
    gap: 40px;
  }
  .card {
    width: 640px;
    height: 366px;
    box-shadow: var(--card-shadow);
    position: relative;
    overflow: hidden;
  }
  .card--back {
    background: var(--navy);
    display: flex;
    align-items: center;
    justify-content: center;
  }
  .wordmark {
    font-weight: 700;
    font-size: 28px;
    letter-spacing: 0.06em;
    text-transform: uppercase;
    white-space: nowrap;
  }
  .card--back .wordmark { color: var(--paper); }
  .card--front { background: var(--paper); }
  .card--front .wordmark {
    position: absolute;
    top: 60px;
    left: 0;
    right: 0;
    text-align: center;
    color: var(--navy);
    font-size: 30px;
  }
  .holder {
    position: absolute;
    left: 36px;
    top: 204px;
    color: var(--navy);
  }
  .holder__name {
    font-weight: 700;
    font-size: 21px;
    letter-spacing: 0.04em;
    text-transform: uppercase;
    line-height: 1.1;
  }
  .holder__title {
    font-weight: 600;
    font-size: 13px;
    margin-top: 2px;
    padding-left: 6px;
  }
  .rule {
    position: absolute;
    left: 36px;
    right: 28px;
    top: 262px;
    height: 8px;
    background: var(--red);
  }
  .contacts {
    position: absolute;
    left: 36px;
    right: 28px;
    top: 284px;
    display: grid;
    grid-template-columns: auto auto;
    justify-content: space-between;
    column-gap: 16px;
    row-gap: 10px;
    font-size: 10.5px;
    font-weight: 600;
    white-space: nowrap;
  }
  .contact__label { color: var(--red); font-weight: 700; }
  .contact__value { color: var(--navy); }
</style>
</head>
<body>
  <main class="stage">
    <section class="card card--back" aria-label="Card back">
      <span class="wordmark">Korvant Solutions Group</span>
    </section>

    <section class="card card--front" aria-label="Card front">
      <span class="wordmark">Korvant Solutions Group</span>

      <div class="holder">
        <p class="holder__name">Gerald Tunstall</p>
        <p class="holder__title">President / CEO</p>
      </div>

      <div class="rule"></div>

      <div class="contacts">
        <p class="contact"><span class="contact__label">Cell : </span><span class="contact__value">555.304.1182</span></p>
        <p class="contact"><span class="contact__label">Office : </span><span class="contact__value">555.617.2093</span></p>
        <p class="contact"><span class="contact__label">Website : </span><span class="contact__value">www.korvantsolutionsgroup.example</span></p>
        <p class="contact"><span class="contact__label">E-Mail : </span><span class="contact__value">geraldt@korvantsolutionsgroup.example</span></p>
      </div>
    </section>
  </main>
</body>
</html>
```